KRL Going Cashless

Hello,
We are a medical office looking to get a flyer created to promote to our patients we will be going "Cashless." Our tagline will be "Cash-Less is Stress-Less"

"Starting in July, to offer you the fastest and most convenient service, we are transitioning to a cashless system. You can now enjoy faster checkout times and greater security with card and contactless payments. More info to come."

I've added two other flyers as sample designs we've used.

Please include logo, addresses, website, phone number

Files to include jpeg, png, pdf (under 5mb), Facebook and Instagram sizing.

Thank you,
Doran

```html
<!DOCTYPE html>
<html lang="en">
<head>
<meta charset="utf-8">
<title>KRL Foot &amp; Ankle – Cash-Less is Stress-Less</title>
<link href="https://fonts.googleapis.com/css2?family=Bebas+Neue&family=League+Spartan:wght@700;800&family=Mrs+Saint+Delafield&family=Poppins:wght@400;500;600;700&display=swap" rel="stylesheet">
<style>
  :root{
    --charcoal:#353535;
    --charcoal-light:#454545;
    --teal:#55c2a4;
    --forest:#3e8a66;
    --orange:#f07f48;
    --white:#ffffff;
    --ink:#222222;
    --page:#ffffff;
  }
  *{box-sizing:border-box;margin:0;padding:0}
  html,body{width:844px;height:1200px;overflow:hidden;background:var(--page)}
  .flyer{
    position:absolute;left:0;top:54px;width:844px;height:1092px;overflow:hidden;
    background:radial-gradient(ellipse at 50% 20%,var(--charcoal-light),var(--charcoal) 70%);
    font-family:"Poppins",sans-serif;
  }
  .backdrop{position:absolute;left:0;top:0;width:844px;height:1092px}
  .brand{
    position:absolute;top:62px;left:0;width:844px;display:flex;justify-content:center;align-items:center;gap:12px;
  }
  .brand-mark{width:22px;height:22px;background:var(--teal)}
  .brand-name{font-family:"Poppins",sans-serif;font-weight:700;font-size:26px;color:var(--orange);letter-spacing:1px}
  .tagline-script{
    position:absolute;top:118px;left:0;width:844px;text-align:center;
    font-family:"Mrs Saint Delafield",cursive;font-size:168px;line-height:1;color:var(--teal);
  }
  .tagline-bold{
    position:absolute;top:300px;left:0;width:844px;text-align:center;
    font-family:"Bebas Neue",sans-serif;font-size:142px;line-height:1;color:var(--orange);letter-spacing:-1px;
  }
  .starting{
    position:absolute;top:448px;left:212px;width:420px;height:70px;background:var(--orange);
    border:1px solid #f6a47c;border-radius:6px;box-shadow:0 4px 6px rgba(0,0,0,.25);
    display:flex;align-items:center;justify-content:center;
    font-family:"League Spartan",sans-serif;font-weight:700;font-size:52px;color:var(--white);letter-spacing:14px;padding-left:14px;padding-top:6px;
  }
  .month{
    position:absolute;top:528px;left:0;width:844px;text-align:center;
    font-family:"League Spartan",sans-serif;font-weight:800;font-size:98px;line-height:1;color:var(--white);letter-spacing:-1px;
  }
  .intro{
    position:absolute;top:632px;left:60px;width:724px;text-align:center;
    font-size:21px;line-height:1.35;color:var(--ink);
  }
  .divider{position:absolute;top:715px;left:44px;width:755px;border-top:1.5px dashed var(--charcoal)}
  .enjoy{
    position:absolute;top:738px;left:47px;
    font-family:"League Spartan",sans-serif;font-weight:800;font-size:60px;line-height:62px;letter-spacing:-1px;
  }
  .enjoy .white{color:var(--white)}
  .enjoy .orange{color:var(--orange)}
  .column-rule{position:absolute;top:742px;left:329px;height:172px;border-left:1.5px dashed var(--charcoal)}
  .benefits{position:absolute;top:742px;left:370px;list-style:none}
  .benefits li{display:flex;align-items:center;gap:12px;height:46px;font-size:26px;font-weight:600;color:var(--charcoal)}
  .benefits svg{width:22px;height:22px;flex:none}
  .more-info{
    position:absolute;top:884px;left:373px;font-family:"Poppins",sans-serif;font-weight:700;font-size:17px;letter-spacing:8.5px;color:var(--white);
  }
  .office{
    position:absolute;top:956px;width:165px;height:87px;background:var(--charcoal);border-radius:2px;
    text-align:center;color:var(--white);padding-top:14px;
  }
  .office .pin{position:absolute;top:-12px;left:71px;width:22px;height:22px}
  .office h3{font-size:12.5px;font-weight:600;color:var(--teal);margin-bottom:3px}
  .office p{font-size:9.5px;line-height:1.4}
  .office-frederick{left:48px}
  .office-martinsburg{left:219px}
  .office-urbana{left:391px}
  .contact-label{position:absolute;top:953px;left:573px;font-weight:700;font-size:13px;letter-spacing:4.5px;color:var(--charcoal)}
  .phone{position:absolute;top:975px;left:573px;display:flex;align-items:center;gap:6px;font-weight:700;font-size:25px;color:var(--white)}
  .phone svg{width:26px;height:26px}
  .website{
    position:absolute;top:1010px;left:571px;width:273px;height:26px;background:var(--orange);
    color:var(--white);font-size:14px;letter-spacing:3px;line-height:26px;padding-left:9px;
  }
  .website b{font-weight:700}
</style>
</head>
<body>
<main class="flyer">
  <svg class="backdrop" viewBox="0 0 844 1092" aria-hidden="true">
    <ellipse cx="422" cy="1000" rx="560" ry="520" fill="var(--forest)"/>
    <ellipse cx="422" cy="1010" rx="520" ry="520" fill="var(--teal)" stroke="var(--charcoal)" stroke-width="1.5"/>
    <rect x="0" y="1000" width="844" height="92" fill="var(--teal)"/>
  </svg>

  <header class="brand">
    <span class="brand-mark"></span>
    <span class="brand-name">KRL FOOT &amp; ANKLE</span>
  </header>

  <h1>
    <span class="tagline-script">Cash-Less</span>
    <span class="tagline-bold">IS STRESS-LESS</span>
  </h1>

  <div class="starting">STARTING</div>
  <div class="month">IN JULY</div>

  <p class="intro">To offer you the fastest and most convenient service, we are transitioning to a cashless system</p>

  <div class="divider"></div>

  <h2 class="enjoy">
    <span class="white">YOU CAN</span><br>
    <span class="orange">NOW</span><br>
    <span class="orange">ENJOY</span>
  </h2>

  <div class="column-rule"></div>

  <ul class="benefits">
    <li><svg viewBox="0 0 22 22"><circle cx="11" cy="11" r="11" fill="var(--orange)"/><path d="M6 11.5l3.3 3.3L16 8" fill="none" stroke="var(--teal)" stroke-width="2.4" stroke-linecap="round" stroke-linejoin="round"/></svg>Faster checkout times</li>
    <li><svg viewBox="0 0 22 22"><circle cx="11" cy="11" r="11" fill="var(--orange)"/><path d="M6 11.5l3.3 3.3L16 8" fill="none" stroke="var(--teal)" stroke-width="2.4" stroke-linecap="round" stroke-linejoin="round"/></svg>Greater security with card</li>
    <li><svg viewBox="0 0 22 22"><circle cx="11" cy="11" r="11" fill="var(--orange)"/><path d="M6 11.5l3.3 3.3L16 8" fill="none" stroke="var(--teal)" stroke-width="2.4" stroke-linecap="round" stroke-linejoin="round"/></svg>Contactless payments</li>
  </ul>

  <p class="more-info">MORE INFO TO COME....</p>

  <section class="office office-frederick">
    <svg class="pin" viewBox="0 0 22 22"><circle cx="11" cy="11" r="11" fill="var(--orange)"/><path d="M11 5a4 4 0 0 0-4 4c0 3 4 7 4 7s4-4 4-7a4 4 0 0 0-4-4z" fill="var(--white)"/><circle cx="11" cy="9" r="1.6" fill="var(--orange)"/></svg>
    <h3>Frederick Office</h3>
    <p>52 Linden Hill Rd.<br>Ste. 110<br>Frederick, MD 21701</p>
  </section>
  <section class="office office-martinsburg">
    <svg class="pin" viewBox="0 0 22 22"><circle cx="11" cy="11" r="11" fill="var(--orange)"/><path d="M11 5a4 4 0 0 0-4 4c0 3 4 7 4 7s4-4 4-7a4 4 0 0 0-4-4z" fill="var(--white)"/><circle cx="11" cy="9" r="1.6" fill="var(--orange)"/></svg>
    <h3>Martinsburg Office</h3>
    <p>78 Orchard View Ct.<br>Martinsburg, WV 25404</p>
  </section>
  <section class="office office-urbana">
    <svg class="pin" viewBox="0 0 22 22"><circle cx="11" cy="11" r="11" fill="var(--orange)"/><path d="M11 5a4 4 0 0 0-4 4c0 3 4 7 4 7s4-4 4-7a4 4 0 0 0-4-4z" fill="var(--white)"/><circle cx="11" cy="9" r="1.6" fill="var(--orange)"/></svg>
    <h3>Urbana Office</h3>
    <p>915 Meadow Park Way<br>Ste. 204<br>Urbana, MD 21704</p>
  </section>

  <p class="contact-label">CONTACT US TODAY</p>
  <p class="phone">
    <svg viewBox="0 0 26 26"><circle cx="13" cy="13" r="13" fill="var(--orange)"/><path d="M9 7l2.5 3-1.4 1.6c.8 1.7 2.1 3 3.8 3.8L15.5 14l3 2.5-1.4 2.2c-4.6-.3-9-4.7-9.3-9.3z" fill="var(--white)"/></svg>
    (555)014-0127
  </p>
  <p class="website">www.<b>stepwellfeet</b>.com</p>
</main>
</body>
</html>
```